Small but growing painting company. Have built up a steady client base. Want to start having a more professional look. Want to start with changing my business cards, and also getting new logo and tee shirts.

Target Market(s)

Home owners, property management companies, all ages 30-70

Industry/Entity Type

Painting And Decorating

Contact Information for Business Card

Bright Ridge Painting LLC Derek Vanstrand 630-485-7039 interior, exterior, vaulted ceiling, drywall repair, pressure washing, kitchen cabinets, epoxy, garage floors,

Font styles to use
Sans Serif
Other font styles liked:
• Harrington

Colors
0355a3
ffffff
ec1f27
000000
3176b5
0493ce
474747
b7b7b7

Requirements
Must have
• Creative, something that doesn’t look like every other painting card.
Nice to have
• I would like something with an arrow or something going to a point

```html
<!DOCTYPE html>
<html lang="en">
<head>
<meta charset="utf-8">
<title>Bright Ridge Painting LLC – Business Card</title>
<link rel="stylesheet" href="https://fonts.googleapis.com/css2?family=Montserrat:wght@500;800&display=swap">
<style>
  :root {
    --brand-red: #ff3b3b;
    --ink: #1c1c1c;
    --backdrop: #e4e4e4;
  }
  * { margin: 0; padding: 0; box-sizing: border-box; }
  html, body {
    width: 1200px;
    height: 1046px;
    overflow: hidden;
    background: var(--backdrop);
    font-family: "Montserrat", Arial, sans-serif;
  }
  .business-card {
    position: absolute;
    left: 50px;
    top: 237px;
    width: 1100px;
    height: 571px;
    overflow: hidden;
    background: var(--brand-red);
  }
  .lower-band {
    position: absolute;
    left: 0;
    top: 283px;
    width: 100%;
    height: 275px;
    background: var(--ink);
  }
  .company-name {
    position: absolute;
    left: 24px;
    top: 160px;
    color: var(--ink);
    font-weight: 800;
    font-size: 44px;
    line-height: 1.05;
    letter-spacing: 0.5px;
    text-transform: uppercase;
    white-space: nowrap;
  }
  .contact-block {
    position: absolute;
    left: 570px;
    top: 168px;
  }
  .person-name {
    color: var(--ink);
    font-weight: 800;
    font-size: 46px;
    line-height: 1;
    letter-spacing: 0.5px;
    text-transform: uppercase;
    white-space: nowrap;
  }
  .phone {
    display: flex;
    align-items: center;
    gap: 8px;
    margin-top: 12px;
    margin-left: 6px;
    color: var(--ink);
    font-weight: 500;
    font-size: 24px;
    letter-spacing: 1px;
  }
  .phone-icon { width: 22px; height: 22px; fill: var(--ink); }
  .services {
    position: absolute;
    left: 570px;
    top: 315px;
    width: 480px;
    color: var(--brand-red);
    font-weight: 500;
    font-size: 16.5px;
    line-height: 24px;
    letter-spacing: 0.6px;
    text-transform: uppercase;
  }
  .services span {
    display: block;
    white-space: nowrap;
    text-align: justify;
    text-align-last: justify;
  }
</style>
</head>
<body>
  <div class="business-card">
    <div class="lower-band"></div>

    <div class="company-name">Bright Ridge<br>Painting LLC</div>

    <div class="contact-block">
      <div class="person-name">Derek Vanstrand</div>
      <div class="phone">
        <svg class="phone-icon" viewBox="0 0 24 24" aria-hidden="true">
          <path d="M6.6 10.8c1.4 2.8 3.8 5.1 6.6 6.6l2.2-2.2c.3-.3.7-.4 1-.2 1.1.4 2.3.6 3.6.6.6 0 1 .4 1 1V20c0 .6-.4 1-1 1C10.6 21 3 13.4 3 4c0-.6.4-1 1-1h3.5c.6 0 1 .4 1 1 0 1.3.2 2.5.6 3.6.1.3 0 .7-.2 1L6.6 10.8z"/>
        </svg>
        <span>630-485-7039</span>
      </div>
    </div>

    <p class="services">
      <span>Interior, Exterior, Vaulted Ceiling,</span>
      <span>Drywall Repair, Pressure Washing,</span>
      <span>Kitchen Cabinets, Epoxy, Garage Floors,</span>
    </p>
  </div>
</body>
</html>
```